Veteran Owned General Contractor needs Bold New Business Cards

We are a service disabled veteran owned small business. We're a general contractor that specializes in excavation, underground utilities, site work, land clearing and demolition. We would like a fresh, simple, bold, new look for our business cards. We're open to ideas! We'd like to incorporate the following information on the card:

Company Name & Logo, Name of Person, Job Title, Office Phone, Fax, Cell Phone, Email Address, Website, SDVOSB

Our logo is included. We look forward to your thoughts.

Thank you!
Updates

Reason: Hello Due to the overwhelming response to this project, we are extending the deadline one time to allow for improved communication and feedback with the top candidates. We would like to thank everyone for their hard work and exceptional creativity! Thank you

Industry/Entity Type

Business

Contact Information for Business Card

Font styles to use
Sans Serif

Requirements
Nice to have
• As we are a veteran owned company, it would be nice to incorporate an American flag into the design. Maybe on the back?

```html
<!DOCTYPE html>
<html lang="en">
<head>
<meta charset="UTF-8">
<title>Brackenfold Business Card</title>
<link rel="stylesheet" href="https://fonts.googleapis.com/css2?family=Montserrat:wght@400;800&display=swap">
<style>
  :root {
    --stage: #7a7a7a;
    --card-dark: #231f20;
    --card-light: #ffffff;
    --green: #6cc04a;
    --text-light: #f2f2f2;
    --badge: #4a4546;
  }
  * { margin: 0; padding: 0; box-sizing: border-box; }
  html, body { width: 1200px; height: 960px; overflow: hidden; }
  body {
    background: var(--stage);
    font-family: "Montserrat", sans-serif;
    position: relative;
  }
  .card {
    position: absolute;
    top: 325px;
    width: 540px;
    height: 310px;
    box-shadow: 0 6px 18px rgba(0,0,0,0.25);
  }
  .card-back { left: 40px; background: var(--card-dark); color: var(--text-light); }
  .card-front { left: 620px; background: var(--card-light); }

  .rule { position: absolute; height: 1.5px; background: var(--green); }
  .rule-top { top: 112px; left: 150px; width: 350px; }
  .rule-bottom { top: 262px; left: 40px; width: 390px; }

  .person { position: absolute; top: 42px; left: 260px; }
  .person-name { font-weight: 800; font-size: 24px; color: var(--green); line-height: 1.1; }
  .person-title { font-size: 15px; margin-top: 4px; }

  .contact { position: absolute; top: 126px; left: 70px; font-size: 14px; line-height: 22px; }
  .contact .label { color: var(--green); }
  .contact .gap { display: inline-block; width: 22px; }

  .badge-slot {
    position: absolute; right: 40px; top: 142px;
    width: 84px; height: 84px; border-radius: 50%;
    background: var(--badge);
  }

  .brand {
    position: absolute; inset: 0;
    display: flex; align-items: center; justify-content: center; gap: 16px;
  }
  .brand-square { width: 42px; height: 42px; background: var(--green); border-radius: 6px; flex: none; }
  .brand-name { font-weight: 800; font-size: 40px; color: var(--green); letter-spacing: 2px; }
</style>
</head>
<body>
  <section class="card card-back">
    <div class="person">
      <div class="person-name">Daniel Reeves</div>
      <div class="person-title">Managing Director</div>
    </div>
    <div class="rule rule-top"></div>
    <div class="contact">
      <div>47B Harwick Lane London NW8 2QT</div>
      <div><span class="label">T</span>: 071.5550.1234<span class="gap"></span><span class="label">M</span>: 071.5550.6789</div>
      <div><span class="label">F</span>: 071.5550.6789</div>
      <div><span class="label">E</span>: info@brackenfold-works.com</div>
      <div><span class="label">W</span>: www.brackenfold-works.com</div>
    </div>
    <div class="badge-slot" role="img" aria-label="Space for a certification badge"></div>
    <div class="rule rule-bottom"></div>
  </section>

  <section class="card card-front">
    <div class="brand">
      <span class="brand-square"></span>
      <span class="brand-name">BRACKENFOLD</span>
    </div>
  </section>
</body>
</html>
```